Quillbase Design Project - App Review

Take a look at this website, gridvault.example. We are creating something very similar to this, four pages are required. The name of our website is BrightPickDigest.example
1) The home page which highlights, app of the day, a carousel which highlights featured apps, and BrightPick in different categories
2) Single App Page - This page will details the app that is selected, app icon, app description, app ratings, and other information you can find on an app page in the lumora market
3) A page that list all the apps in a category, for example if the user select, "100 BrightPick" the page that will display the list of 100 apps, 10 per page, summary of description, a small icon, screenshot etc for each app
4) Review Page - where we review an app of the day, including screenshots, videos, text reviews etc
I do not have any logo at the moment, use these as nav links; home, my apps, reviews, blog and contact. Thank you.
I will like to see a nice creativity. I am open to a very beautiful color combinations. Thank you
Target Market(s)
App shoppers, people that are looking for new apps, discounted apps etc
Industry/Entity Type
Store
Look and feel

```html
<!DOCTYPE html>
<html lang="en">
<head>
<meta charset="utf-8">
<title>BrightPick – The greatest apps website</title>
<link href="https://fonts.googleapis.com/css2?family=Arimo:wght@400;700&family=Open+Sans:wght@400;600;700&family=Kalam:wght@700&display=swap" rel="stylesheet">
<style>
:root{
  --bg:#262626;
  --bg-dark:#1e1e1e;
  --header:#2e2e2e;
  --line:#3b3b3b;
  --text:#c9c9c9;
  --text-soft:#a9a9a9;
  --white:#f2f2f2;
  --blue:#1f9ad8;
  --blue-dark:#0f6ea8;
  --green:#7cb32b;
  --green-dark:#4f7d18;
  --yellow:#f2d34a;
  --screen:#2b2b2b;
  --frame:#0c0c0c;
}
*{margin:0;padding:0;box-sizing:border-box}
html,body{width:1200px;height:693px;overflow:hidden}
body{position:relative;background:radial-gradient(ellipse at 60% 40%,#2c2c2c,var(--bg) 60%,var(--bg-dark));font-family:Arimo,Arial,sans-serif;color:var(--text)}
.site-header{position:absolute;left:0;top:0;width:1200px;height:52px;background:linear-gradient(#333,var(--header));border-bottom:1px solid var(--line)}
.site-header .pointer{position:absolute;left:589px;top:52px}
.social{position:absolute;left:169px;top:19px;display:flex;gap:9px}
.social span{width:21px;height:21px;border-radius:50%;background:#6b6b6b}
.main-nav{position:absolute;top:18px;left:0;font-size:12px;color:#cfcfcf}
.main-nav a{position:absolute;color:inherit;text-decoration:none;white-space:nowrap}
.brand-mark{position:absolute;left:161px;top:138px;width:60px;height:60px;border-radius:50%;background:#0b0b0b}
.brand-name{position:absolute;left:242px;top:148px;font-family:"Open Sans",sans-serif;font-weight:400;font-size:32px;line-height:1.2;color:var(--blue);white-space:nowrap}
.tagline{position:absolute;left:243px;top:194px;font-family:"Open Sans",sans-serif;font-size:17.5px;color:var(--white);letter-spacing:.4px;white-space:nowrap}
.intro{position:absolute;left:160px;top:251px;width:316px;text-align:right;font-size:12.2px;letter-spacing:.45px;line-height:16px;color:var(--text-soft)}
.dl-btn{position:absolute;top:371px;width:135px;height:47px;border-radius:4px;padding:9px 0 0 46px;color:#fff;font-family:"Open Sans",sans-serif}
.dl-btn small{display:block;font-size:8.5px;opacity:.85;line-height:11px}
.dl-btn strong{display:block;font-size:14.5px;line-height:17px}
.dl-btn i{position:absolute;left:14px;top:12px;width:22px;height:22px;border-radius:50%;background:rgba(255,255,255,.25)}
.dl-nimbus{left:172px;background:linear-gradient(#3bb3ea,var(--blue-dark))}
.dl-orbit{left:333px;background:linear-gradient(#8ec83a,var(--green-dark))}
.offer-arrow{position:absolute;left:300px;top:428px}
.offer{position:absolute;left:180px;width:284px;top:470px;text-align:center;font-family:Kalam,cursive;font-weight:700;font-size:17px;color:#fff;letter-spacing:.5px}
.aotd-title{position:absolute;left:171px;width:285px;top:529px;text-align:center;font-weight:700;font-size:15.5px;color:#fff;letter-spacing:.5px}
.aotd{position:absolute;left:171px;top:556px;width:285px;height:59px;border-radius:5px;background:linear-gradient(#8cc63f,var(--green-dark));box-shadow:0 2px 4px rgba(0,0,0,.5)}
.aotd .chev{position:absolute;top:22px}
.aotd-icon{position:absolute;left:25px;top:6px;width:46px;height:46px;border-radius:3px;border:2px solid #f4e9a0;background:linear-gradient(135deg,#f2a93b,#d24a3a 55%,#3b7fc2)}
.aotd-name{position:absolute;left:88px;top:9px;font-family:"Open Sans",sans-serif;font-size:17px;font-weight:600;color:#fff;white-space:nowrap;letter-spacing:.3px}
.aotd-buy{position:absolute;left:89px;top:32px;font-family:"Open Sans",sans-serif;font-size:12.5px;font-weight:700;color:var(--yellow)}
.divider{position:absolute;left:533px;top:116px;width:1px;height:490px;background:linear-gradient(transparent,#3a3a3a 20%,#3a3a3a 80%,transparent)}
.tablet{position:absolute;left:642px;top:108px;width:379px;height:483px;border-radius:30px;background:linear-gradient(160deg,#222,var(--frame) 40%);border:3px solid #d8d8d8;box-shadow:0 0 0 1px #777,0 10px 20px rgba(0,0,0,.6)}
.tablet-home{position:absolute;left:178px;top:450px;width:22px;height:22px;border-radius:50%;border:2px solid #2a2a2a;background:#080808}
.screen{position:absolute;left:684px;top:153px;width:295px;height:393px;background:var(--screen);overflow:hidden}
.status{height:13px;background:#1b1b1b;font-size:8px;color:#9a9a9a;padding:2px 0 0 8px;position:relative}
.status .batt{position:absolute;right:6px;top:4px;width:12px;height:5px;background:#cfcfcf;border-radius:1px}
.app-art{position:absolute;left:11px;top:33px;width:141px;height:108px;border:1px solid #777;background:radial-gradient(ellipse at 45% 55%,#c7783a,#7a3d1c 45%,#2a1a12)}
.app-title{position:absolute;left:167px;top:37px;font-size:15.5px;color:#fff;white-space:nowrap}
.app-platform{position:absolute;left:167px;top:57px;font-size:11px;color:#e6e6e6}
.price{position:absolute;left:186px;top:76px;width:57px;height:47px;border-radius:7px;background:#fff;text-align:center;font-size:16px;color:#222;padding-top:5px}
.price span{position:absolute;left:5px;bottom:5px;width:47px;height:11px;border-radius:6px;background:linear-gradient(#9ad34a,#4c8f1e);font-size:6.5px;color:#fff;font-weight:700;line-height:11px}
.checks{position:absolute;left:168px;top:132px;font-size:10px;color:#e6e6e6;display:flex;gap:12px}
.checks label{display:flex;align-items:center;gap:6px}
.checks i{width:12px;height:12px;background:#fff;border-radius:2px}
.app-desc{position:absolute;left:12px;top:161px;width:268px;font-size:10.2px;line-height:14.2px;color:#e4e4e4;hyphens:auto}
.app-desc p{margin-bottom:6px}
.dots{position:absolute;left:748px;top:625px;display:flex;gap:7px}
.dots span{width:28px;height:3px;background:#555}
.dots .active{background:#999}
.site-footer{position:absolute;left:468px;top:657px;width:238px;height:20px;background:#1e1e1e;text-align:center;font-size:10.8px;line-height:20px;color:#9c9c9c}
</style>
</head>
<body>
<header class="site-header">
  <div class="social" aria-label="Social links"><span></span><span></span><span></span><span></span></div>
  <nav class="main-nav">
    <a style="left:657px">Home</a>
    <a style="left:727px">My Apps</a>
    <a style="left:812px">Reviews</a>
    <a style="left:898px">blog</a>
    <a style="left:958px">Contact</a>
  </nav>
  <svg class="pointer" width="22" height="12" viewBox="0 0 22 12"><path d="M0 0H22L11 11Z" fill="#2e2e2e" stroke="#3b3b3b"/></svg>
</header>

<div class="brand-mark"></div>
<div class="brand-name">BrightPick</div>
<div class="tagline">The greatest apps website</div>
<p class="intro">Lorem ipsum dolor sit amet, consectetur adipisicing elit, sed do eiusmod tempor incididunt ut labore et dolore magna aliqua. Ut enim ad minim veniam, quis nostrud exercitation ullamco laboris nisi ut aliquip ex ea commodo consequat.</p>

<a class="dl-btn dl-nimbus"><i></i><small>Download now for</small><strong>Nimbus</strong></a>
<a class="dl-btn dl-orbit"><i></i><small>Download now for</small><strong>Orbit</strong></a>

<svg class="offer-arrow" width="40" height="36" viewBox="0 0 40 36"><path d="M5 31C20 32 30 22 33 6" fill="none" stroke="#fff" stroke-width="1.6"/><path d="M28 10L34 3L36 12" fill="none" stroke="#fff" stroke-width="1.6"/></svg>
<div class="offer">only $3.1 limited offer!</div>

<div class="aotd-title">APP OF THE DAY !!</div>
<div class="aotd">
  <svg class="chev" style="left:8px" width="10" height="14" viewBox="0 0 10 14"><path d="M8 2L3 7L8 12" fill="none" stroke="#fff" stroke-width="2.5"/></svg>
  <div class="aotd-icon" role="img" aria-label="App icon artwork"></div>
  <div class="aotd-name">Minibus Dash HD</div>
  <div class="aotd-buy">BUY NOW !!</div>
  <svg class="chev" style="left:267px" width="10" height="14" viewBox="0 0 10 14"><path d="M2 2L7 7L2 12" fill="none" stroke="#fff" stroke-width="2.5"/></svg>
</div>

<div class="divider"></div>

<div class="tablet"><div class="tablet-home"></div></div>
<section class="screen">
  <div class="status">Slate<span class="batt"></span></div>
  <div class="app-art" role="img" aria-label="Game cover artwork for the featured app"></div>
  <div class="app-title">Dream Seeker</div>
  <div class="app-platform">Nova OS Universal</div>
  <div class="price">FREE<span>BUY NOW</span></div>
  <div class="checks"><label><i></i>Own it</label><label><i></i>Want it</label></div>
  <div class="app-desc">
    <p>VALDRIN | The Orrenmoor Chronicles is a text adventure in the same vein as the classic “Pick Your Own Path” books from yesteryear with a few RPG elements thrown in for fun.</p>
    <p>However, this game comes with a twist... YOU will truly decide the fate of Orrenmoor as this is just part one of a six-part story.</p>
    <p>BUT! You only pay once and the rest of the story will be yours till completion. (NO in app purchases whatsoever.)</p>
    <p>Of course, there is a catch...</p>
    <p>The story will be continued through download content added via updates AND it is completely based on download numbers. For every 500 downloads, we will add 100 pages of content until the story is completed. That's right; every download counts towards the next chapter.</p>
  </div>
</section>

<div class="dots"><span></span><span></span><span></span><span class="active"></span><span></span></div>

<footer class="site-footer">brightpick &nbsp;©&nbsp; 2013. All Rights Reserved</footer>
</body>
</html>
```